verdant manor grounds simple classy business card design

my name is owen brackley and I run a gardening business aimed at high class verdant manor grounds. the business name is verdant manor grounds and our logo was designed on brief hive .My clientel are anything from residential homes to businesses. I take pride in my work and know that I offer a service like no other in my area.
The business card will be used to represent my business and I want it to be not only rememberable, but simplistic and modern. Eye catching too. Of course I would like it relatable to gardening and appealing to the correct clientel - those being garden enthusiasts, prestigious homes and businesses that are after top of the line gardening services like no other on the market.
I am not a typical lawn mowing business so I don't want a typical card design that represents that. The gardens I work with are generally million dollar properties with owners who are very garden proud looking for upkeep and guidance from me along with sometimes whole new garden designs. I want the business cards to show to my clients that I take pride, as they do, in their garden. And I want them to know from my card that I am a professional, qualified horticulturist offering them a top of the line service for life. I want them to refer my business on. I want them to look at my business card and see class and professionalism in a modern unique bold way.
The card should be simple with the possibility of the logo on the front being embossed/debossed and my details on the back the card should have a organic garden feel it's very important to me that it is absolutely perfect
I am also very open to ideas and suggestions so look forward to seeing the designs. the business logo has been supplied with this project and I want the card to be double sided

Contact info is
Owen Brackley - Managing Director / Horticulturist
Phone : 0481 562 907
Email: owenbrackley@verdantmanorgrounds.example.au

Target Market(s)

high class gardens residential and commercial

Industry/Entity Type

Gardener

Contact Information for Business Card

Contact info is
Phone : 0481 562 907

PLEASE MAKE CARD DOUBLE SIDED

Requirements
Must have
• organic simple classy modern feel
• must flow with the current logo that has been supplied with this project
• Double sided
• Must explain in a simple way that I deal with high end gardens and I'm a qualified horticulturist
Nice to have
• embossed debossed logo
Should not have
• shouldn't be to busy or cheap looking

```html
<!DOCTYPE html>
<html lang="en">
<head>
<meta charset="utf-8">
<title>Verdant Manor Grounds – Business Card</title>
<link rel="stylesheet" href="https://fonts.googleapis.com/css2?family=Source+Sans+3:wght@400;600;700&display=swap">
<style>
  :root {
    --backdrop: #e9e4dc;
    --card: #fbfbf9;
    --card-edge: #dcd8d0;
    --leaf-green: #4fa83a;
    --ink: #2e2e2e;
    --ink-soft: #444444;
    --emboss: #ecebe7;
    --emboss-shade: #d4d2cc;
  }
  * { box-sizing: border-box; margin: 0; padding: 0; }
  html, body {
    width: 1200px;
    height: 794px;
    overflow: hidden;
    background: var(--backdrop);
    font-family: "Source Sans 3", "Myriad Pro", Arial, sans-serif;
  }
  .card-set {
    position: relative;
    width: 1200px;
    height: 794px;
    display: flex;
    align-items: center;
    justify-content: center;
    gap: 44px;
  }
  .card {
    width: 536px;
    height: 306px;
    background: var(--card);
    border: 1px solid var(--card-edge);
    box-shadow: 0 6px 18px rgba(60, 50, 40, 0.12);
    display: flex;
    flex-direction: column;
    align-items: center;
  }

  /* Details side */
  .card--details { padding-top: 34px; }
  .holder-name {
    color: var(--leaf-green);
    font-weight: 700;
    font-size: 22px;
    letter-spacing: 0.5px;
    text-transform: uppercase;
    line-height: 1;
  }
  .holder-role {
    margin-top: 6px;
    color: var(--ink);
    font-weight: 600;
    font-size: 15px;
    text-transform: uppercase;
    letter-spacing: 0.2px;
  }
  .emboss-mark {
    margin-top: 16px;
    width: 74px;
    height: 74px;
    border-radius: 50%;
    background: var(--emboss);
    box-shadow: inset 1px 1px 2px rgba(255,255,255,0.9), inset -1px -2px 3px var(--emboss-shade);
  }
  .contact-list {
    margin-top: 26px;
    list-style: none;
    text-align: center;
    color: var(--ink-soft);
    font-size: 16px;
    line-height: 1.3;
  }
  .contact-label {
    color: var(--leaf-green);
    font-weight: 700;
  }

  /* Brand side */
  .card--brand {
    justify-content: center;
    gap: 18px;
  }
  .brand-dot {
    width: 92px;
    height: 92px;
    border-radius: 50%;
    background: var(--leaf-green);
  }
  .brand-name {
    color: var(--leaf-green);
    font-weight: 600;
    font-size: 34px;
    letter-spacing: 4px;
    text-transform: uppercase;
  }
</style>
</head>
<body>
  <main class="card-set">
    <section class="card card--details" aria-label="Card back with contact details">
      <h1 class="holder-name">Owen Brackley</h1>
      <p class="holder-role">Managing Director / Horticulturist</p>
      <div class="emboss-mark" aria-hidden="true"></div>
      <ul class="contact-list">
        <li><span class="contact-label">Phone:</span> 0481 562 907</li>
        <li>owenbrackley@verdantmanorgrounds.example.au</li>
        <li>www.verdantmanorgrounds.example.au</li>
      </ul>
    </section>

    <section class="card card--brand" aria-label="Card front with business name">
      <div class="brand-dot" aria-hidden="true"></div>
      <p class="brand-name">Verdant Manor Grounds</p>
    </section>
  </main>
</body>
</html>
```